Redesign of an insurance website

Attached is an insurance website that I need to redesign. Currently the website is too dark. I like for example www.brenvalo.com . Could you make the website lighter and change the structure a little so that it is more user friendly?

Industry/Entity Type

Insurance

Number of Pages Required

4 page

```html
<!DOCTYPE html>
<html lang="en">
<head>
<meta charset="utf-8">
<title>Kryvano – FAQ's</title>
<link rel="stylesheet" href="https://fonts.googleapis.com/css2?family=Poppins:wght@300;400;600;700&display=swap">
<style>
:root{
  --blue:#29b9ec;
  --blue-soft:#5ec8ef;
  --ink:#1b1b1b;
  --text:#2a2a2a;
  --header-bg:#f2fafd;
  --item-bg:#f6f7f8;
  --white:#ffffff;
}
*{box-sizing:border-box;margin:0;padding:0}
html,body{width:1200px;height:1102px;overflow:hidden;background:var(--white)}
body{font-family:'Poppins',sans-serif;color:var(--text);position:relative}
.topbar{height:30px;background:var(--blue);display:flex;align-items:center;justify-content:space-between;padding:0 119px 0 121px}
.social{display:flex;gap:12px}
.social span{width:12px;height:12px;border-radius:50%;background:var(--white);display:block}
.account{display:flex;gap:26px;color:var(--white);font-size:11.5px;font-weight:300}
.account a{display:flex;align-items:center;gap:5px;color:inherit;text-decoration:none}
.header{height:57px;background:var(--header-bg);position:relative}
.search{position:absolute;left:121px;top:24px;width:132px;height:26px;border:2px solid #e6eef2;border-radius:14px;background:var(--white);font-size:10.5px;color:#777;padding:4px 0 0 14px;font-weight:300}
.search svg{position:absolute;right:14px;top:5px}
.brand{position:absolute;left:0;right:0;top:26px;text-align:center;font-size:24px;font-weight:700;color:var(--ink);letter-spacing:.5px;display:flex;justify-content:center;align-items:center;gap:8px}
.brand i{width:12px;height:12px;border-radius:50%;background:var(--blue);display:block}
.nav{position:absolute;right:119px;top:35px;display:flex;gap:17px;font-size:14px;font-weight:400}
.nav a{color:var(--ink);text-decoration:none}
.nav a.active{color:var(--blue)}
.hero{height:155px;background:linear-gradient(100deg,#5aa3c9 0%,#6cc6e8 45%,#8fd6ee 70%,#6cc4e4 100%);color:var(--white);text-align:center;padding-top:54px}
.hero h1{font-size:27px;font-weight:600;letter-spacing:1px;line-height:1.2}
.hero p{font-size:12px;font-weight:300;margin-top:2px}
.faq{position:absolute;left:121px;top:288px;width:960px}
.faq-q{height:37px;background:var(--item-bg);display:flex;align-items:center;justify-content:space-between;padding:0 16px;font-size:14px;font-weight:300;color:var(--ink);margin-bottom:1.6px}
.faq-q.open{background:var(--blue);color:var(--white);margin-bottom:0}
.faq-a{padding:11px 14px 14px;font-size:12.3px;line-height:20px;font-weight:300;color:#333}
.newsletter{position:absolute;left:0;top:860px;width:1200px;height:242px;background:linear-gradient(100deg,#3fb8e8 0%,#56c3ec 50%,#47bbe8 100%)}
.card{position:absolute;left:165px;top:29px;width:862px;height:143px;background:var(--white);border-radius:12px}
.card h2{position:absolute;left:49px;top:42px;font-size:24px;font-weight:600;color:var(--blue);letter-spacing:.5px}
.card p{position:absolute;left:49px;top:76px;font-size:17px;font-weight:300;color:var(--ink)}
.form{position:absolute;left:343px;top:54px;width:469px;height:39px}
.form .email{position:absolute;left:0;top:0;width:300px;height:39px;border:1px solid #d8d8d8;border-radius:20px 0 0 20px;font-size:12.5px;font-weight:300;padding:11px 0 0 27px;color:#333}
.form .btn{position:absolute;right:0;top:0;width:192px;height:39px;border-radius:20px;background:var(--ink);color:var(--white);font-size:14.5px;font-weight:400;text-align:center;line-height:39px}
.rule{position:absolute;left:0;top:199px;width:1200px;height:1px;background:rgba(255,255,255,.35)}
.copy{position:absolute;left:0;right:0;top:211px;text-align:center;color:var(--white);font-size:12.5px;font-weight:300}
</style>
</head>
<body>
<div class="topbar">
  <div class="social"><span></span><span></span><span></span><span></span></div>
  <div class="account">
    <a href="#"><svg width="10" height="11" viewBox="0 0 10 11"><circle cx="5" cy="3" r="2.6" fill="#fff"/><path d="M0 11c0-3 2-4.5 5-4.5s5 1.5 5 4.5z" fill="#fff"/></svg>SIGN IN</a>
    <a href="#"><svg width="9" height="11" viewBox="0 0 9 11"><path d="M2 5V3.5a2.5 2.5 0 0 1 5 0V5" stroke="#fff" stroke-width="1.4" fill="none"/><rect x="0" y="5" width="9" height="6" rx="1" fill="#fff"/></svg>SIGN UP</a>
  </div>
</div>
<header class="header">
  <div class="search">Search...
    <svg width="12" height="12" viewBox="0 0 12 12"><circle cx="5" cy="5" r="3.8" stroke="#29b9ec" stroke-width="1.8" fill="none"/><path d="M8 8l3 3" stroke="#29b9ec" stroke-width="1.8"/></svg>
  </div>
  <div class="brand"><i></i>KRYVANO.CZ</div>
  <nav class="nav"><a href="#">ABOUT US</a><a href="#" class="active">FAQ'S</a><a href="#">CONTACT US</a></nav>
</header>
<section class="hero" role="img" aria-label="Photo of hands holding a card over a desk, tinted blue">
  <h1>FAQ'S</h1>
  <p>HOME/FAQ'S</p>
</section>
<section class="faq">
  <div class="faq-q open">Praesent ut turpis a arcu fringilla auctor
    <svg width="13" height="8" viewBox="0 0 13 8"><path d="M1 7l5.5-5.5L12 7" stroke="#fff" stroke-width="1.6" fill="none"/></svg></div>
  <div class="faq-a">Praesent ut turpis a arcu fringilla auctor. Praesent posuere, orci sit amet rhoncus tincidunt, erat justo mattis enim, vitae accumsan ligula enim ut urna. Donec consectetur turpis at ex pharetra, et semper sem aliquet. Vestibulum ante ipsum primis in faucibus orci luctus et ultrices posuere cubilia Curae; Nullam molestie consectetur magna ac pulvinar. Duis facilisis eleifend ultricies. Class aptent taciti sociosqu ad litora torquent per, per inceptos himenaeos. Curabitur tincidunt eget augue quis fringilla. Morbi hendrerit turpis sit amet aliquet lobortis. Proin gravida placerat porta. Morbi at tincidunt ipsum. Aenean mattis justo aliquet, dictum neque ut, pharetra urna. Aliquam eu lacinia ligula. Cras volutpat placerat purus in pulvinar. Sed eget consequat ipsum, vitae egestas nunc. Aenean non venenatis augue.</div>
  <div class="faq-q">Sed tempus nunc dui, eget vulputate tortor laoreet nec<svg width="13" height="8" viewBox="0 0 13 8"><path d="M1 1l5.5 5.5L12 1" stroke="#222" stroke-width="1.6" fill="none"/></svg></div>
  <div class="faq-q">Vivamus in risus imperdiet quam molestie sollicitudin vitae aliquet lectus<svg width="13" height="8" viewBox="0 0 13 8"><path d="M1 1l5.5 5.5L12 1" stroke="#222" stroke-width="1.6" fill="none"/></svg></div>
  <div class="faq-q">Aliquam porta ex nec arcu pharetra luctus<svg width="13" height="8" viewBox="0 0 13 8"><path d="M1 1l5.5 5.5L12 1" stroke="#222" stroke-width="1.6" fill="none"/></svg></div>
  <div class="faq-q">Integer cursus condimentum magna id<svg width="13" height="8" viewBox="0 0 13 8"><path d="M1 1l5.5 5.5L12 1" stroke="#222" stroke-width="1.6" fill="none"/></svg></div>
  <div class="faq-q">Nulla mattis augue vitae bibendum scelerisque<svg width="13" height="8" viewBox="0 0 13 8"><path d="M1 1l5.5 5.5L12 1" stroke="#222" stroke-width="1.6" fill="none"/></svg></div>
  <div class="faq-q">Pellentesque interdum venenatis bibendum<svg width="13" height="8" viewBox="0 0 13 8"><path d="M1 1l5.5 5.5L12 1" stroke="#222" stroke-width="1.6" fill="none"/></svg></div>
  <div class="faq-q">Integer cursus condimentum magna id<svg width="13" height="8" viewBox="0 0 13 8"><path d="M1 1l5.5 5.5L12 1" stroke="#222" stroke-width="1.6" fill="none"/></svg></div>
  <div class="faq-q">Nulla mattis augue vitae bibendum scelerisque<svg width="13" height="8" viewBox="0 0 13 8"><path d="M1 1l5.5 5.5L12 1" stroke="#222" stroke-width="1.6" fill="none"/></svg></div>
  <div class="faq-q">Pellentesque interdum venenatis bibendum<svg width="13" height="8" viewBox="0 0 13 8"><path d="M1 1l5.5 5.5L12 1" stroke="#222" stroke-width="1.6" fill="none"/></svg></div>
</section>
<footer class="newsletter" role="img" aria-label="Photo of people working at a desk with papers, tinted blue">
  <div class="card">
    <h2>SIGNUP NEWSLETTER</h2>
    <p>Get In Touch With Us</p>
    <div class="form"><div class="email">Enter Email Address</div><div class="btn">SUBSCRIBE NOW</div></div>
  </div>
  <div class="rule"></div>
  <div class="copy">Copyright © 2017 Kryvano. All right reserved.</div>
</footer>
</body>
</html>
```